Carpet cleaning company focused on high quality needs business cards

We are a growing company that just merged with another company and need to design a new business card. We do both residential as well as commercial cleaning. We do carpet, tile & grout, upholstery, hard floors, and stain & pet odor removal. We treat our customers like family and strive to achieve outstanding results with every job.

```html
<!DOCTYPE html>
<html lang="en">
<head>
<meta charset="utf-8">
<title>Brightwell Floor Care – Business Cards</title>
<link href="https://fonts.googleapis.com/css2?family=Open+Sans:wght@400;600;700;800&display=swap" rel="stylesheet">
<style>
  :root {
    --backdrop: #232323;
    --card: #ffffff;
    --red: #ee4540;
    --blue: #0284c7;
    --ink: #111111;
    --mascot-red: #ec4a3f;
    --mascot-blue: #1f78b8;
  }
  * { box-sizing: border-box; margin: 0; padding: 0; }
  html, body {
    width: 1200px; height: 780px; overflow: hidden;
    background: var(--backdrop);
    font-family: "Open Sans", Arial, sans-serif;
    color: var(--ink);
  }
  .sheet { position: relative; width: 1200px; height: 780px; }
  .card {
    position: absolute; top: 236px;
    width: 540px; height: 309px;
    background: var(--card);
    border-radius: 22px;
    overflow: hidden;
    box-shadow: 0 10px 24px rgba(0,0,0,.55);
  }
  .card--front { left: 40px; }
  .card--back { left: 620px; }

  /* brand lockup */
  .brand { position: absolute; display: flex; align-items: center; }
  .brand__mascot {
    flex: none;
    background: linear-gradient(135deg, var(--mascot-blue) 0 38%, var(--mascot-red) 38% 100%);
  }
  .brand__name { font-weight: 800; color: var(--ink); line-height: 1.05; }
  .card--front .brand { left: 118px; top: 52px; }
  .card--front .brand__mascot { width: 150px; height: 132px; }
  .card--front .brand__name { font-size: 28px; margin-left: 16px; width: 170px; }
  .card--back .brand { left: 74px; top: 118px; }
  .card--back .brand__mascot { width: 96px; height: 86px; }
  .card--back .brand__name { font-size: 16px; margin-left: 10px; width: 100px; }

  /* services */
  .services { position: absolute; left: 40px; right: 40px; top: 206px; text-align: center; }
  .services__heading {
    display: flex; align-items: center; gap: 8px;
    color: var(--red); font-weight: 700; font-size: 11px; letter-spacing: .5px;
  }
  .services__heading::before, .services__heading::after {
    content: ""; flex: 1; height: 1px; background: var(--red);
  }
  .services__list {
    list-style: none; display: flex; flex-wrap: wrap; justify-content: center;
    gap: 3px 12px; margin-top: 7px; font-size: 11.5px;
  }
  .services__list li::before {
    content: ""; display: inline-block; width: 6px; height: 6px; border-radius: 50%;
    background: var(--red); margin-right: 5px; vertical-align: 1px;
  }

  /* back */
  .backdrop-curves { position: absolute; inset: 0; width: 100%; height: 100%; }
  .divider { position: absolute; left: 290px; top: 40px; width: 1px; height: 175px; background: var(--ink); }
  .contact { position: absolute; left: 306px; top: 54px; }
  .contact__name { font-size: 23px; font-weight: 800; line-height: 1.1; }
  .contact__first { color: var(--red); }
  .contact__last { color: var(--blue); }
  .contact__role { font-size: 13px; font-weight: 600; margin-bottom: 10px; }
  .contact__line { display: flex; align-items: center; gap: 8px; font-size: 12px; margin-top: 4px; }
  .contact__line svg { width: 12px; height: 12px; fill: var(--red); flex: none; }
  .address { position: absolute; left: 100px; top: 256px; font-size: 13px; }
</style>
</head>
<body>
<main class="sheet">

  <section class="card card--front">
    <div class="brand">
      <div class="brand__mascot" role="img" aria-label="Mascot illustration: cleaning technician holding a steam wand on a red square"></div>
      <p class="brand__name">Brightwell Floor Care</p>
    </div>
    <div class="services">
      <h2 class="services__heading">OUR SERVICES</h2>
      <ul class="services__list">
        <li>Both residential as well as commercial cleaning</li>
        <li>Carpet</li>
        <li>Tile &amp; grout</li>
        <li>Upholstery</li>
        <li>Hard floors</li>
        <li>Stain &amp; pet odor removal</li>
      </ul>
    </div>
  </section>

  <section class="card card--back">
    <svg class="backdrop-curves" viewBox="0 0 540 309" preserveAspectRatio="none" aria-hidden="true">
      <path d="M0 0 H120 Q45 70 32 309 H0 Z" fill="var(--red)"/>
      <path d="M540 95 Q505 235 385 309 H540 Z" fill="var(--blue)"/>
    </svg>
    <div class="brand">
      <div class="brand__mascot" role="img" aria-label="Mascot illustration: cleaning technician holding a steam wand on a red square"></div>
      <p class="brand__name">Brightwell Floor Care</p>
    </div>
    <div class="divider"></div>
    <div class="contact">
      <p class="contact__name"><span class="contact__first">Marta</span> <span class="contact__last">Novakova</span></p>
      <p class="contact__role">Managing Director</p>
      <p class="contact__line">
        <svg viewBox="0 0 24 24"><path d="M6.6 10.8a15 15 0 0 0 6.6 6.6l2.2-2.2a1 1 0 0 1 1-.25 11.4 11.4 0 0 0 3.6.57 1 1 0 0 1 1 1V20a1 1 0 0 1-1 1A17 17 0 0 1 3 4a1 1 0 0 1 1-1h3.5a1 1 0 0 1 1 1c0 1.25.2 2.45.57 3.57a1 1 0 0 1-.25 1z"/></svg>
        (555) 014-2758
      </p>
      <p class="contact__line">
        <svg viewBox="0 0 24 24"><path d="M2 5h20v14H2z M4 7v.5l8 5 8-5V7z" fill-rule="evenodd"/></svg>
        info@brightwellcare.com
      </p>
      <p class="contact__line">
        <svg viewBox="0 0 24 24"><circle cx="12" cy="12" r="10"/></svg>
        www.brightwellcare.com
      </p>
    </div>
    <p class="address">1840 Meadowbrook Ave. Suite 310 Riverton, TX 76000</p>
  </section>

</main>
</body>
</html>
```